Plumbing Trifold Design for Restoration Company

We would like this brochure to match our current KVT branding and marketing materials. The overall look should feel modern, clean, premium, and trustworthy.

Our brand colors are included in the attached files along with a picture of what our current marketing material looks like. We'd like to use real KVT photography whenever possible rather than stock images, but if stock images are necessary, please go ahead and use.

The brochure should communicate that KVT is a full-service plumbing company backed by years of experience in both traditional plumbing and complex pipe restoration.

Front Page: we would like to include logo, phone number (800-318-4957), website (www.kvtflow.example) and then maybe the following: "Traditional Plumbing Services", "residential & commercial, 24/7 Emergency Service, Licensed & Insured" and can also add "reliable Repairs. Honest Service. Lasting Solutions" if spacing allows.

Other sections we would like included (not in any particular order):

-Why Choose KVT?:
Family-oriented team
Licensed & insured professionals
Residential & commercial expertise
Honest recommendations
Quality workmanship
Emergency service available
Clean, respectful technicians
One trusted company for plumbing and sewer solutions
____________________________
Our Story:
Built on solving complex plumbing challenges. Trusted for every plumbing need.
Since our founding, Conduit Renewal Partners has built a reputation for helping homeowners, businesses, and property managers solve some of the industry’s most challenging plumbing and sewer problems through quality workmanship, professionalism, and innovative solutions.
As our customers’ needs have grown, so has our commitment to serving them. What began as a leader in pipe restoration has expanded into full-service plumbing, allowing us to provide complete plumbing solutions—from everyday repairs and fixture replacements to water heaters, drain cleaning, repiping, and emergency plumbing services.
Today, our traditional plumbing division delivers the same level of expertise, communication, and customer care that KVT has become known for. Whether it’s a simple repair or a complex plumbing project, our goal remains the same: to provide dependable solutions, lasting quality, and an exceptional customer experience every step of the way.
-Our Values:
The KVT Way
Professional - Don't settle for good, BE GREAT
Responsive - When there's a need, BE FIRST!
Service - Life is not about you, BE ABOUT OTHERS!
These three values guide everything we do
Complete Plumbing Solutions:
-Plumbing Repairs
Reliable solutions to keep your plumbing system running safely and efficiently.
Leak detection & repair
Pipe Burst Repairs
Water line repairs
Whole-home repiping

-Fixtures & Installations
Professional installation, repair, and replacement of the fixtures you use every day.
Faucets
Toilets
Sinks
Showers & tubs
Garbage disposals
Hose bibs
Shut-off valves

-Water Heater Services
Whether you need a repair, replacement, or routine maintenance, we'll keep your hot water flowing.
Water heater repair
Water heater replacement
Tankless water heaters
Expansion tanks
Recirculation pumps
Preventative maintenance

-Drain & Sewer Solutions
From routine drain cleaning to complete sewer repairs, our team has the equipment and expertise to get your plumbing flowing again.
Drain cleaning
Hydro jetting
Camera inspections
Main sewer line cleaning
Sewer line repair
Sewer line replacement
Emergency drain backups
maybe add in a blurb saying
"Need a Trenchless Solution?
Ask about our non-invasive solutions as an alternative to traditional replacement for sewer and storm drain systems"
Testimonials:
"This company is fantastic, very professional and knowledgeable. Use them at several of my communities I manage and highly recommend them!" Belvine Townhomes
"KVT continues to be the primary plumbing vendor I use for all of my properties throughout Tampa Bay!" Corliss Dunes Condominium
"KVT did a great job at a great price and have always been willing to help with their abundance of knowledge prior to even working on projects for our community!" Townhomes at Hollow Fern
"KVT is amazing! My office flooded out on a Friday night and they responded within a couple hours to make the needed repair. The team was professional and got right to work (there van was also immaculate, which tells you a lot about hot they operate). Would definitely recommend them to anyone!" Dorin Welsby
______________________
Ready to get started?
Whether it's a leaking pipe, a new water heater, a clogged drain, or a plumbing emergency, our team is here to help
800-318-4957
info@kvtflow.example
www.kvtflow.example

Additional Information: please feel free to edit any of the pictures provided and AI files can be provided for the other marketing material if helpful. We would like an AI file and PDF ready print if possible.
Thank you!

commercial and residential property owners

Plumbing

Colors
0054AA
0677BA
7BADD7
CADEEF
E8F1F8

Must have
• My project must flow with current marketing material colors
Nice to have
• would like the front page picture to fade nicely into background

```html
<!DOCTYPE html>
<html lang="en">
<head>
<meta charset="utf-8">
<title>KVT Trifold Brochure</title>
<link rel="stylesheet" href="https://fonts.googleapis.com/css2?family=Russo+One&family=Arimo:wght@400;700&display=swap">
<style>
:root{
  --navy:#1c2030;
  --navy-deep:#151826;
  --card:#232839;
  --blue:#0054AA;
  --blue-mid:#0677BA;
  --blue-bright:#1e8fd8;
  --blue-light:#7BADD7;
  --blue-pale:#CADEEF;
  --blue-mist:#E8F1F8;
  --white:#ffffff;
  --ink:#1c2236;
  --muted:#a9b1c4;
  --star:#f6c21c;
  --stage:#a4a4a4;
}
*{box-sizing:border-box;margin:0;padding:0}
html,body{width:1200px;height:3423px;overflow:hidden;background:var(--stage)}
body{position:relative;font-family:"Arimo",Arial,sans-serif;color:var(--white)}
.head{font-family:"Russo One","Arimo",sans-serif;font-weight:400}
.spread{position:absolute;left:49px;width:1102px;height:780px;background:var(--navy);overflow:hidden}
.spread.outside{top:900px}
.spread.inside{top:1740px;background:var(--white)}
.abs{position:absolute}
.pipes{position:absolute;left:0;top:0;pointer-events:none}

/* outside left panel */
.trench-top{left:0;top:0;width:367px;height:300px;background:var(--navy)}
.badge{left:50px;top:38px;width:70px;height:76px;border:3px solid var(--blue-bright);text-align:center;color:var(--blue-bright);line-height:1}
.badge .big{font-family:"Russo One",sans-serif;font-size:30px;display:block;margin-top:6px}
.badge .small{font-family:"Russo One",sans-serif;font-size:11px;display:block;margin-top:3px}
.trench-title{left:145px;top:28px;font-size:28px;line-height:32px}
.trench-title span{color:var(--blue-bright)}
.social-label{left:48px;top:142px;font-size:12px}
.social{left:50px;top:164px;display:flex;gap:12px}
.social i{width:16px;height:16px;border-radius:50%;background:var(--blue-mid);display:block}
.trench-copy{left:145px;top:136px;width:210px;font-size:11px;line-height:15px}
.why{left:0;top:213px;width:340px;height:567px;background:var(--white);color:var(--ink)}
.why h2{position:absolute;left:33px;top:42px;font-size:25px;color:var(--blue)}
.why ul{position:absolute;left:33px;top:92px;width:290px;list-style:none}
.why li{height:36.6px;line-height:34px;font-size:15.5px;font-weight:700;border-bottom:1px solid #e3e7ee;padding-left:22px;position:relative}
.why li::before{content:"";position:absolute;left:2px;top:12px;border-left:10px solid var(--blue);border-top:6px solid transparent;border-bottom:6px solid transparent}
.why .trust{position:absolute;left:33px;top:353px;width:280px;font-size:15px;line-height:19px}
.van{left:18px;top:413px;width:310px;height:128px;border-radius:8px;background:linear-gradient(180deg,#f4f6f9,#d7dde6)}

/* testimonials */
.testi-title{left:367px;width:368px;top:28px;text-align:center;font-size:30px;color:var(--blue-bright)}
.card{left:411px;width:282px;background:var(--card);border-radius:6px;text-align:center;padding:10px 12px 0}
.card p{font-size:10px;line-height:13px;color:#e6e9f0}
.card .who{font-family:"Arimo",sans-serif;font-weight:700;font-style:italic;color:var(--blue-bright);font-size:12px;margin-top:6px}
.stars{color:var(--star);font-size:17px;letter-spacing:1px;line-height:20px}
.ready{left:367px;width:368px;top:548px;text-align:center;font-size:25px;line-height:29px}
.ready span{color:var(--blue-bright)}
.ready-copy{left:440px;width:224px;top:609px;text-align:center;font-size:10.5px;line-height:13px}
.contact-band{left:367px;top:680px;width:368px;height:100px;background:var(--navy-deep)}
.contact{left:455px;font-size:20px;font-weight:700;color:var(--white);display:flex;align-items:center;gap:8px}
.contact.blue{color:var(--blue-bright)}
.contact svg{flex:none}

/* cover */
.cover-strip{left:735px;top:0;width:367px;height:780px;background:var(--navy)}
.logo{display:flex;align-items:center;gap:10px}
.logo .mark{width:30px;height:30px;background:var(--blue-bright);flex:none}
.logo .name{font-family:"Russo One",sans-serif;font-size:52px;line-height:1;color:var(--white);letter-spacing:4px}
.logo-sub{font-size:11px;letter-spacing:3px;color:var(--white)}
.cover-box{left:760px;top:120px;width:320px;height:425px;background:var(--blue-mid);border-radius:10px;overflow:hidden}
.cover-box .label{position:absolute;left:0;top:0;width:100%;height:150px;background:linear-gradient(90deg,var(--blue),var(--blue-mid))}
.cover-box .trad{position:absolute;left:26px;top:22px;font-size:22px;letter-spacing:1px}
.cover-box .big{position:absolute;left:26px;top:50px;font-size:40px;line-height:42px}
.cover-photo{position:absolute;left:10px;top:152px;width:300px;height:263px;border-radius:0 0 8px 8px;background:linear-gradient(180deg,#7e8a96 0%,#c9cfd6 45%,#3d4656 100%)}
.feature{top:570px;width:112px;text-align:center;font-size:11px;line-height:13px;color:#dfe5ef}
.feature svg{display:block;margin:0 auto 6px}
.cover-phone{left:735px;width:367px;top:683px;text-align:center;font-size:36px}
.cover-web{left:735px;width:367px;top:727px;text-align:center;font-size:14px;letter-spacing:8px;color:var(--blue-bright)}
.cover-tag{left:735px;width:367px;top:751px;text-align:center;font-size:9.5px;color:var(--muted);letter-spacing:.5px}

/* inside */
.values{left:0;top:0;width:367px;height:340px;background:var(--navy)}
.values h2{position:absolute;left:0;width:100%;top:28px;text-align:center;font-size:27px;color:var(--blue-bright)}
.values .way{position:absolute;left:0;width:100%;top:66px;text-align:center;font-size:13px}
.value{position:absolute;top:190px;width:90px;text-align:center;font-size:10.5px;line-height:13px}
.value b{display:block;font-size:11px;margin-bottom:2px}
.values .guide{position:absolute;left:0;width:100%;top:278px;text-align:center;font-size:12px}
.story{left:0;top:340px;width:367px;height:440px;background:var(--white);color:var(--ink)}
.story h2{position:absolute;left:32px;top:17px;font-size:26px;color:var(--blue)}
.story .body{position:absolute;left:32px;top:66px;width:312px;font-size:11px;line-height:13.6px;text-align:justify;hyphens:auto}
.story .body p{margin-bottom:10px}
.services{left:385px;top:32px;width:708px;height:620px;background:var(--navy);border-radius:14px}
.services h2{position:absolute;left:30px;top:50px;font-size:36px}
.svc{position:absolute;width:300px}
.svc h3{font-family:"Russo One",sans-serif;font-weight:400;font-size:19px;color:var(--blue-bright);display:flex;align-items:center;gap:10px}
.svc .desc{font-size:13px;line-height:16.5px;margin-top:10px;color:#e4e8ef}
.svc ul{list-style:none;margin-top:12px;font-size:13px;line-height:17.8px}
.svc li{padding-left:16px;position:relative}
.svc li::before{content:"";position:absolute;left:0;top:4px;border-left:7px solid var(--blue-bright);border-top:4.5px solid transparent;border-bottom:4.5px solid transparent}
.svc .cols{display:flex;gap:40px}
.heater-photo{left:367px;top:668px;width:363px;height:112px;background:linear-gradient(180deg,#3f4a5a,#1f2634)}
.in-phone{left:730px;width:372px;top:692px;text-align:center;font-size:34px;color:var(--blue)}
.in-web{left:730px;width:372px;top:735px;text-align:center;font-size:14px;letter-spacing:8px;color:var(--blue)}
.in-tag{left:730px;width:372px;top:757px;text-align:center;font-size:9.5px;color:#4a5468}
</style>
</head>
<body>

<!-- OUTSIDE SPREAD -->
<section class="spread outside">
  <div class="abs trench-top"></div>
  <div class="abs badge"><span class="big">24/7</span><span class="small">EMERGENCY<br>SERVICE</span></div>
  <h2 class="abs trench-title head">Need a<br><span>Trenchless<br>Solution?</span></h2>
  <div class="abs social-label">Social Media</div>
  <div class="abs social"><i></i><i></i><i></i></div>
  <p class="abs trench-copy">Ask about our non-invasive solutions as an alternative to traditional replacement for sewer and storm drain systems</p>

  <div class="abs why">
    <h2 class="head">Why Choose KVT?</h2>
    <ul>
      <li>Family-oriented team</li>
      <li>Licensed &amp; insured professionals</li>
      <li>Residential &amp; commercial expertise</li>
      <li>Honest recommendations</li>
      <li>Quality workmanship</li>
      <li>Emergency service available</li>
      <li>Clean, respectful technicians</li>
    </ul>
    <p class="trust">One trusted company for plumbing and sewer solutions</p>
    <div class="abs van" role="img" aria-label="White KVT service van photograph"></div>
  </div>

  <h2 class="abs testi-title head">Testimonials</h2>
  <div class="abs card" style="top:76px;height:99px">
    <p>"This company is fantastic, very professional and knowledgeable. Use them at several of my communities I manage and highly recommend them!"</p>
    <div class="who">Belvine Townhomes</div><div class="stars">★★★★★</div>
  </div>
  <div class="abs card" style="top:185px;height:88px">
    <p>"KVT continues to be the primary plumbing vendor I use for all of my properties throughout Tampa Bay!"</p>
    <div class="who">Corliss Dunes Condominium</div><div class="stars">★★★★★</div>
  </div>
  <div class="abs card" style="top:284px;height:102px">
    <p>"KVT did a great job at a great price and have always been willing to help with their abundance of knowledge prior to even working on projects for our community!"</p>
    <div class="who">Townhomes at Hollow Fern</div><div class="stars">★★★★★</div>
  </div>
  <div class="abs card" style="top:397px;height:145px">
    <p>"KVT is amazing! My office flooded out on a Friday night and they responded within a couple hours to make the needed repair. The team was professional and got right to work (there van was also immaculate, which tells you a lot about hot they operate). Would definitely recommend them to anyone!"</p>
    <div class="who">Dorin Welsby</div><div class="stars">★★★★★</div>
  </div>
  <h2 class="abs ready head">Ready To<br><span>Get Started?</span></h2>
  <p class="abs ready-copy">Whether it's a leaking pipe, a new water heater, a clogged drain, or a plumbing emergency, our team is here to help</p>
  <div class="abs contact-band"></div>
  <div class="abs contact" style="top:693px">
    <svg width="16" height="16" viewBox="0 0 16 16"><circle cx="8" cy="8" r="8" fill="var(--blue-bright)"/><path d="M5 4l2 2-1 1.2a5 5 0 0 0 2.8 2.8L10 9l2 2-1.2 1.2C7.5 12 4 8.5 3.8 5.2z" fill="#fff"/></svg>800-318-4957</div>
  <div class="abs contact blue" style="top:718px">
    <svg width="16" height="16" viewBox="0 0 16 16"><circle cx="8" cy="8" r="8" fill="var(--blue-bright)"/><rect x="4" y="5" width="8" height="6" fill="#fff"/><path d="M4 5l4 3 4-3" stroke="var(--blue-bright)" fill="none"/></svg>info@kvtflow.example</div>
  <div class="abs contact blue" style="top:743px">
    <svg width="16" height="16" viewBox="0 0 16 16"><circle cx="8" cy="8" r="8" fill="var(--blue-bright)"/><circle cx="8" cy="8" r="4.5" fill="none" stroke="#fff"/><path d="M3.5 8h9M8 3.5v9" stroke="#fff"/></svg>www.kvtflow.example</div>

  <div class="abs cover-strip"></div>
  <div class="abs logo" style="left:808px;top:34px"><span class="mark"></span><span class="name">KVT</span></div>
  <div class="abs logo-sub" style="left:808px;top:92px">CONDUIT RENEWAL PARTNERS</div>
  <div class="abs cover-box">
    <div class="label"></div>
    <div class="trad head">— TRADITIONAL —</div>
    <div class="big head">PLUMBING<br>SERVICES</div>
    <div class="cover-photo" role="img" aria-label="Technician carrying hose beside service van, fading into background"></div>
  </div>
  <div class="abs feature" style="left:748px">
    <svg width="30" height="30" viewBox="0 0 30 30" fill="none" stroke="#fff" stroke-width="2"><rect x="6" y="6" width="18" height="20"/><path d="M10 11h3M17 11h3M10 16h3M17 16h3M13 26v-5h4v5"/></svg>Residential<br>commercial<br>Services</div>
  <div class="abs feature" style="left:862px">
    <svg width="30" height="30" viewBox="0 0 30 30" fill="none" stroke="#fff" stroke-width="2"><circle cx="15" cy="15" r="11"/><path d="M15 8v7l5 3"/></svg>24/7<br>Emergency<br>Service</div>
  <div class="abs feature" style="left:975px">
    <svg width="30" height="30" viewBox="0 0 30 30" fill="none" stroke="#fff" stroke-width="2"><path d="M7 4h12l5 5v17H7z"/><path d="M11 12h9M11 16h9M11 20h5"/></svg>Licensed<br>&amp; Insured<br>Services</div>
  <div class="abs cover-phone head">800-318-4957</div>
  <div class="abs cover-web head">WWW.KVTFLOW.EXAMPLE</div>
  <div class="abs cover-tag">Reliable Repairs | Honest Service | Lasting Solutions</div>

  <svg class="pipes" width="1102" height="780" viewBox="0 0 1102 780" fill="none" stroke-linecap="butt">
    <path d="M12 0V190Q12 206 28 206H300Q340 206 340 246V780" stroke="var(--blue)" stroke-width="9"/>
    <path d="M12 0V150" stroke="#fff" stroke-width="9"/>
    <path d="M340 260V410" stroke="#fff" stroke-width="9"/>
    <path d="M4 150h16M332 260h16M332 410h16" stroke="#fff" stroke-width="5"/>
    <path d="M745 780V540Q745 530 755 530" stroke="var(--blue)" stroke-width="9"/>
    <path d="M1090 0V120M1084 25h12" stroke="#fff" stroke-width="7"/>
    <path d="M1090 540V560Q1090 570 1080 570" stroke="#fff" stroke-width="8"/>
    <path d="M1094 520v55" stroke="var(--blue)" stroke-width="8"/>
  </svg>
</section>

<!-- INSIDE SPREAD -->
<section class="spread inside">
  <div class="abs values">
    <h2 class="head">Our Values</h2>
    <div class="way">The KVT Way</div>
    <svg class="abs" style="left:0;top:88px" width="367" height="100" viewBox="0 0 367 100" fill="none">
      <path d="M58 48A45 45 0 0 0 148 48A45 45 0 0 0 236 48A45 45 0 0 0 326 48" stroke="var(--blue-mid)" stroke-width="8"/>
      <circle cx="100" cy="45" r="33" fill="var(--blue-mist)" stroke="var(--blue-mid)" stroke-width="4"/>
      <circle cx="191" cy="45" r="33" fill="var(--blue-mist)" stroke="var(--blue-mid)" stroke-width="4"/>
      <circle cx="284" cy="45" r="33" fill="var(--blue-mist)" stroke="var(--blue-mid)" stroke-width="4"/>
      <g stroke="var(--navy)" stroke-width="2">
        <circle cx="100" cy="37" r="5"/><circle cx="88" cy="41" r="4"/><circle cx="112" cy="41" r="4"/><path d="M90 57q10-12 20 0"/>
        <rect x="178" y="33" width="26" height="17"/><path d="M186 56h10M191 50v6"/>
        <circle cx="284" cy="45" r="9"/><circle cx="284" cy="45" r="3"/>
      </g>
    </svg>
    <div class="value" style="left:55px"><b>Professional</b>Don't settle for good, BE GREAT</div>
    <div class="value" style="left:146px"><b>Responsive</b>When there's a need, BE FIRST!</div>
    <div class="value" style="left:239px"><b>Service</b>Life is not about you, BE ABOUT OTHERS!</div>
    <div class="guide">These three values guide everything we do</div>
  </div>

  <div class="abs story">
    <h2 class="head">Our Story</h2>
    <div class="body">
      <p>Built on solving complex plumbing challenges. Trusted for every plumbing need.</p>
      <p>Since our founding, Conduit Renewal Partners has built a reputation for helping homeowners, businesses, and property managers solve some of the industry's most challenging plumbing and sewer problems through quality workmanship, professionalism, and innovative solutions.</p>
      <p>As our customers' needs have grown, so has our commitment to serving them. What began as a leader in pipe restoration has expanded into full-service plumbing, allowing us to provide complete plumbing solutions—from everyday repairs and fixture replacements to water heaters, drain cleaning, repiping, and emergency plumbing services.</p>
      <p>Today, our traditional plumbing division delivers the same level of expertise, communication, and customer care that KVT has become known for. Whether it's a simple repair or a complex plumbing project, our goal remains the same: to provide dependable solutions, lasting quality, and an exceptional customer experience every step of the way.</p>
    </div>
  </div>

  <div class="abs services">
    <h2 class="head">Complete Plumbing Solutions</h2>
    <div class="svc" style="left:18px;top:120px">
      <h3><svg width="22" height="22" viewBox="0 0 22 22" fill="none" stroke="#fff" stroke-width="2"><path d="M4 18l8-8M12 10l3-6 4 4-6 3"/></svg>Plumbing Repairs</h3>
      <p class="desc">Reliable solutions to keep your plumbing system running safely and efficiently.</p>
      <ul><li>LEAK DETECTION &amp; REPAIR</li><li>PIPE BURST REPAIRS</li><li>WATER LINE REPAIRS</li><li>WHOLE-HOME REPIPING</li></ul>
    </div>
    <div class="svc" style="left:18px;top:313px">
      <h3><svg width="22" height="22" viewBox="0 0 22 22" fill="none" stroke="#fff" stroke-width="2"><path d="M3 19L19 3M3 3l16 16"/></svg>Fixtures &amp; Installations</h3>
      <p class="desc">Professional installation, repair, and replacement of the fixtures you use every day.</p>
      <div class="cols">
        <ul><li>FAUCETS</li><li>TOILETS</li><li>SINKS</li><li>SHOWERS &amp; TUBS</li></ul>
        <ul><li>GARBAGE<br>DISPOSALS</li><li>HOSE BIBS</li><li>SHUT-OFF VALVES</li></ul>
      </div>
    </div>
    <div class="svc" style="left:382px;top:120px">
      <h3><svg width="22" height="22" viewBox="0 0 22 22" fill="none" stroke="#fff" stroke-width="2"><rect x="5" y="3" width="12" height="17" rx="2"/><circle cx="11" cy="13" r="3"/></svg>Water Heater Services</h3>
      <p class="desc">Whether you need a repair, replacement, or routine maintenance, we'll keep your hot water flowing.</p>
      <ul><li>WATER HEATER REPAIR</li><li>WATER HEATER REPLACEMENT</li><li>TANKLESS WATER HEATERS</li><li>EXPANSION TANKS</li><li>RECIRCULATION PUMPS</li><li>PREVENTATIVE MAINTENANCE</li></ul>
    </div>
    <div class="svc" style="left:382px;top:352px">
      <h3><svg width="22" height="22" viewBox="0 0 22 22" fill="none" stroke="#fff" stroke-width="2"><path d="M4 8h14v4H4zM8 12v7h6v-7M11 2v6"/></svg>Drain &amp; Sewer Solutions</h3>
      <p class="desc">From routine drain cleaning to complete sewer repairs, our team has the equipment and expertise to get your plumbing flowing again.</p>
      <ul><li>DRAIN CLEANING</li><li>HYDRO JETTING</li><li>CAMERA INSPECTIONS</li><li>MAIN SEWER LINE CLEANING</li><li>SEWER LINE REPAIR</li><li>SEWER LINE REPLACEMENT</li><li>EMERGENCY DRAIN BACKUPS</li></ul>
    </div>
    <div class="abs logo" style="left:20px;top:508px"><span class="mark" style="width:40px;height:40px"></span><span class="name" style="font-size:62px">KVT</span></div>
    <div class="abs logo-sub" style="left:20px;top:578px;font-size:12.5px;letter-spacing:3.5px">CONDUIT RENEWAL PARTNERS</div>
  </div>

  <div class="abs heater-photo" role="img" aria-label="Water heater pipe fittings close-up photograph"></div>
  <div class="abs in-phone head">800-318-4957</div>
  <div class="abs in-web head">WWW.KVTFLOW.EXAMPLE</div>
  <div class="abs in-tag">Reliable Repairs | Honest Service | Lasting Solutions</div>

  <svg class="pipes" width="1102" height="780" viewBox="0 0 1102 780" fill="none">
    <path d="M12 0V320Q12 336 28 336H340Q355 336 355 351V780" stroke="var(--blue)" stroke-width="9"/>
    <path d="M12 0V130M4 130h16" stroke="#fff" stroke-width="8"/>
    <path d="M385 0V20M1093 40V650" stroke="var(--blue)" stroke-width="6"/>
    <path d="M1093 480V600M1085 480h16M1085 600h16" stroke="#fff" stroke-width="6"/>
    <path d="M385 45V70M377 45h16" stroke="#fff" stroke-width="6"/>
  </svg>
</section>

</body>
</html>
```